Modellprojekt in der Jugendhilfe sucht für Abschlussbroschüre ansprechendes Design
Zielgruppe
Wir sind ein Jugendhilfeträger und haben kürzlich ein dreijähriges Modellprojekt 'Qualitätsmarke-Gemeinsame Familienbegleitung' (Signet 'QM_Anerkennung' liegt anbei) beendet. Zielgruppen sind zum Einen Kinder und Jugendliche, die in Erziehungshilfe-Wohngruppen leben und zum Anderen Fach- und Führungskräfte in der Kinder- und Jugendhilfe. Über Ablauf und Schlussfolgerungen aus dem abgeschlossenen Modellprojekt soll eine 30-seitige Broschüre mit dem Titel 'Hier wächst Mitsprache' Untertitel 'Ein Wegweiser zur Qualitätsmarke' Auskunft geben.
Aufgabenstellung
- Broschüre im DIN A4 - Format,
- Dummy-Text für Projektstruktur und -beteiligte,
- Formschönes und dynamisches Design,
- Platzhalter für eigene Bilder (max. 3 pro Seite),
- die 6 Einrichtungslogos in einer Reihe auf dem Deckblatt vorne (unten),
- Der Broschüreninhalt ist in der PDF 'Kurzvorstellung enthalten',
- Vorgaben zum CD im PDF 'Hauptmanual KWF',
- Das KWF-Signet, wie im Manual beschrieben,
- das ebenfalls hochgeladene Gütesiegel kommt auf das Deckblatt

```html
<!DOCTYPE html>
<html lang="de">
<head>
<meta charset="utf-8">
<title>Hier wächst Mitsprache – Innenseiten</title>
<link rel="stylesheet" href="https://fonts.googleapis.com/css2?family=Open+Sans:wght@400;600;700;800&display=swap">
<style>
  :root {
    --brand-blue: #0b5f9e;
    --brand-blue-dark: #064f87;
    --ink: #3a3a3a;
    --muted: #6d6d6d;
    --paper: #f7f7f7;
    --stage: #e6e6e6;
  }
  * { box-sizing: border-box; margin: 0; padding: 0; }
  html, body { width: 1200px; height: 845px; overflow: hidden; }
  body {
    background: var(--stage);
    font-family: "Open Sans", Arial, sans-serif;
    color: var(--ink);
  }
  .spread {
    position: absolute;
    left: 49px; top: 32px;
    width: 1102px; height: 781px;
    display: flex;
    box-shadow: 0 6px 24px rgba(0,0,0,.18);
  }
  .page {
    position: relative;
    width: 551px; height: 781px;
    background: var(--paper);
    overflow: hidden;
  }
  .page--left { border-right: 1px solid #d8d8d8; }

  .running-head {
    position: absolute; top: 34px; left: 30px; right: 30px;
    display: flex; align-items: center; gap: 8px;
    font-size: 6.5px; color: var(--muted);
  }
  .running-head__rule { flex: 1; height: 1.5px; background: var(--brand-blue); }

  .section-title {
    font-weight: 800; text-transform: uppercase;
    letter-spacing: .06em; color: var(--brand-blue);
    font-size: 15px; line-height: 1.2;
  }
  .body-copy {
    font-size: 8.6px; line-height: 1.5;
    text-align: justify; hyphens: auto;
  }
  .body-copy + .body-copy { margin-top: 9px; }

  .story { position: absolute; top: 62px; left: 30px; right: 30px; }
  .story .section-title { margin-bottom: 6px; }

  .photo-kids {
    position: absolute; top: 212px; left: 0; width: 551px; height: 250px;
    background: radial-gradient(ellipse at 55% 60%, #d9dfe2 0%, #c9b8b4 22%, transparent 45%),
                linear-gradient(180deg, #6f8f45 0%, #8aa85a 45%, #5f7d35 100%);
  }

  .mission { position: absolute; top: 486px; left: 30px; right: 30px; }
  .mission .section-title { margin-bottom: 8px; }

  .folio {
    position: absolute; bottom: 22px;
    font-size: 7px; font-weight: 600;
  }
  .page--left .folio { right: 30px; color: var(--muted); }
  .page--right .folio { right: 30px; color: #fff; }

  .photo-road {
    position: absolute; top: 0; left: 0; width: 551px; height: 470px;
    background: radial-gradient(ellipse at 85% 18%, #f4e9a8 0%, #cdbf74 18%, transparent 42%),
                linear-gradient(180deg, #6e6a66 0%, #8e8a6a 35%, #8c9a4c 55%, #5a5a52 75%, #3c3c3c 100%);
  }
  .feature {
    position: absolute; top: 470px; left: 0; width: 551px; height: 311px;
    background: var(--brand-blue);
    padding: 32px 30px 0;
    color: #fff;
  }
  .feature .section-title { color: #e8eef4; font-size: 14.5px; margin-bottom: 10px; }
  .feature .body-copy { color: #f2f6fa; }
</style>
</head>
<body>
<main class="spread">
  <section class="page page--left">
    <header class="running-head">
      <span class="running-head__label">Reisegepäck</span>
      <span class="running-head__rule"></span>
    </header>

    <article class="story">
      <h2 class="section-title">Erfolgsstory</h2>
      <p class="body-copy">Lorem ipsum dolor sit amet, graecequidameoste, facetediceretvituperatoribusest at. Odioeratmnesarchumeiusu, neclabiturlobortis at. Est albucius mandamus et. Ut pro option omnesque, accusatapartiendosedte.Euiusatquiignota maiorum. His nominaviexpetendainteresset an, te vitae abhorreanteum. Eiharumfierent vel. Eos eutheophrastusdefinitionem. Quo appeteretractatossententiae id, ut duo hinctempor, omnesnominavisadipscingeumei. Necutnonumylaborelobortis, quod interessetpersequeris cu qui. Cu cum oportereconcludaturque. Intellegamcomprehensam in pro. Cum an dicam consul vivendo, no mutatdolore qui. Aperiri maiorum percipitur no sed, eu duo posse atomorum, scriptablanditfabellas in qui. Ius no iustoornatusdissentiet, cibovirislibrisvel in. At cibosententiaeius. Necea alia libris, eum tale utamuroporteat no. Eos euwisiomittampertinacia, temporequidemfierentvixte.</p>
    </article>

    <div class="photo-kids" role="img" aria-label="Foto: vier Kinder geben sich im Park ein High-Five"></div>

    <article class="mission">
      <h2 class="section-title">Unser Selbstverständnis</h2>
      <p class="body-copy">Der Mensch ist uns wichtig und steht in unserer Arbeit stets im Mittelpunkt. Wir setzen an den Stärken und Fähigkeiten unserer Betreuten und Klienten an, um die individuellen Potentiale für eine gelingende (Weiter-)Entwicklung zu nutzen oder dafür zu aktivieren. Wir sehen den Menschen immer eingebettet in ein soziales Gefüge von Freunden, Eltern und Verwandten. Die Familien möglichst mitzunehmen und somit die Hilfen so gut es geht ganzheitlich auszurichten, ist uns ein großes Anliegen.</p>
      <p class="body-copy">Unsere Angebote haben stets das Ziel, notwendige Betreuung oder Unterstützung so intensiv wie nötig, aber auch so kurz wie möglich zu gestalten.</p>
      <p class="body-copy">Dabei greifen wir auf über 50 Jahre innovative Jugendhilfeerfahrung zurück, auf deren Grundlage wir ständig neue, den jeweiligen Bedarfen und Bedingungen angepasste Unterstützungsmöglichkeiten entwickeln.</p>
    </article>

    <span class="folio">02</span>
  </section>

  <section class="page page--right">
    <div class="photo-road" role="img" aria-label="Foto: Mädchen mit rotem Rucksack geht auf einer Landstraße dem Sonnenaufgang entgegen"></div>

    <article class="feature">
      <h2 class="section-title">Hier wächst Mitsprache – eine partizipative Lernreise</h2>
      <p class="body-copy">Lorem ipsum dolor sit amet, graecequidameoste, facetediceretvituperatoribusest at. Odioeratmnesarchumeiusu, neclabiturlobortis at. Est albucius mandamus et. Ut pro option omnesque, accusatapartiendosedte.Euiusatquiignota maiorum. His nominaviexpetendainteresset an, te vitae abhorreanteum. Eiharumfierent vel. Eos eutheophrastusdefinitionem. Quo appeteretractatossententiae id, ut duo hinctempor, omnesnominavisadipscingeumei. Necutnonumylaborelobortis, quod interessetpersequeris cu qui. Cu cum oportereconcludaturque. Intellegamcomprehensam in pro. Cum an dicam consul vivendo, no mutatdolore qui. Aperiri maiorum percipitur no sed, eu duo posse atomorum, scriptablanditfabellas in qui. Ius no iustoornatusdissentiet, cibovirislibrisvel in. At cibosententiaeius. Necea alia libris, eum tale utamuroporteat no. Eos euwisiomittampertinacia, temporequidemfierentvixte.</p>
    </article>

    <span class="folio">03</span>
  </section>
</main>
</body>
</html>
```